Lend a Lantern Website Design (design layout only)

We need a website design for a new nonprofit organization based in Des Moines, Iowa called Lend a Lantern. The nonprofit provides soccer training opportunities to youth soccer players looking to improve their game while also affecting the lives of the less fortunate in a positive way. While participating in the training programs the players also go out and raise money for selected charities. The organization then donates the funds. In its first 18 months we donated $10,500. We would like to see designs attempt to symbolize the mission of the nonprofit - essentially "improve you while improving someone else."

We would like to see the following features:

· A place to donate - Our intent is to have the home page linked to the donation page; a simple straight-forward process for people to give money, and make donating as painless as possible - no account needed to make a donation, credit card or e-check should be the only information needed to donate, and have it be on a single page.

· A photo gallery so people can browse the photo gallery to get a better understanding of our organization and a place to add videos and a calendar to show upcoming events

· A place for contact information and the profiles of directors and board members. This should include a spot showing all the charities the organization donates to. Also includes a news section/blog for comments and suggestions.

We want the design to revolve around the content and mission. We would really like to stress our organization as nonprofit. We would also like if the website was user friendly and easy to navigate.

The logo of our organization is uploaded

```html
<!DOCTYPE html>
<html lang="en">
<head>
<meta charset="utf-8">
<title>Lend a Lantern — Home</title>
<link href="https://fonts.googleapis.com/css2?family=Bitter:ital,wght@0,400;0,700;1,400&family=Arimo:wght@400;700&display=swap" rel="stylesheet">
<style>
:root{
  --green:#6f9a3e;
  --green-dark:#4c7a2b;
  --green-deep:#3d6a22;
  --footer:#7ea24f;
  --footer-bar:#5e8636;
  --field:#97b872;
  --grey:#8a8a8a;
  --text:#555;
  --line:#d6d6d6;
  --white:#fff;
}
*{box-sizing:border-box;margin:0;padding:0}
html,body{width:878px;height:1200px;overflow:hidden}
body{position:relative;background:var(--white);font-family:Arimo,Arial,sans-serif;color:var(--text);font-size:9px}
.abs{position:absolute}
.slab{font-family:Bitter,Georgia,serif}

/* header */
.brand{left:122px;top:30px;width:110px;font-family:Bitter,Georgia,serif;font-weight:700;color:var(--green);font-size:21px;line-height:21px;text-transform:uppercase;letter-spacing:.5px}
.btn-donate{left:648px;top:21px;width:110px;height:25px;background:var(--green-dark);color:var(--white);font-family:Bitter,serif;font-weight:700;font-size:12px;letter-spacing:.6px;display:flex;align-items:center;justify-content:center;border-radius:3px;box-shadow:1px 2px 2px rgba(0,0,0,.3)}
.phone{left:636px;top:58px;display:flex;align-items:center;gap:6px;color:var(--green-dark);font-size:15px;font-weight:700}
.nav{left:352px;top:88px;display:flex;gap:13px;font-size:10.5px;color:#222}
.nav .active{color:var(--green);display:flex;align-items:center;gap:2px}

/* hero */
.hero{left:0;top:116px;width:878px;height:307px;background:radial-gradient(ellipse at 40% 45%,#5f8a3c 0%,#456f2a 55%,#2f4f1c 100%)}
.hero-arrow{top:338px}
.mission{left:0;top:402px;width:878px;text-align:center;color:var(--white);font-family:Bitter,serif;font-weight:700;font-size:14px;letter-spacing:.4px;text-shadow:0 1px 2px rgba(0,0,0,.6)}

/* welcome */
h2{font-family:Bitter,serif;font-weight:700;font-size:16px;color:var(--green)}
h2 span{color:var(--grey)}
.welcome{left:118px;top:438px;width:416px}
.welcome p{margin-top:5px;line-height:11.7px;font-size:8.6px}
.welcome .more{color:var(--green-deep);font-weight:700}
.welcome .lead{margin-top:10px;font-family:Bitter,serif;font-style:italic;font-size:10.6px;line-height:13.6px;color:#555}
.video-title{left:549px;top:438px}
.video{left:549px;top:464px;width:210px;height:131px;background:linear-gradient(135deg,#d8d2c8,#b43a32 55%,#7a2a25);border:1px solid #555}
.video .bar{position:absolute;left:0;bottom:0;width:100%;height:20px;background:#1b1b1b}
.video .progress{position:absolute;left:0;bottom:20px;width:100%;height:3px;background:#cc1f1f}

/* gallery */
.gallery{left:122px;top:617px;width:634px;height:149px;border:2px solid #b5ca9a;border-radius:6px}
.gallery h2{position:absolute;left:6px;top:4px;font-size:14px}
.gallery .nav-arrows{position:absolute;right:10px;top:7px;font-size:13px;color:#444;letter-spacing:4px}
.thumbs{position:absolute;left:4px;top:30px;display:flex;gap:8px}
.thumb{width:118px;height:100px;background:#fff;border:1px solid #e2e2e2;padding:4px;box-shadow:0 4px 4px -2px rgba(0,0,0,.25)}
.thumb div{width:100%;height:100%}

/* tabs */
.tabs{display:flex;gap:6px;position:absolute}
.tab{height:21px;padding:0 6px;border:1px solid var(--line);border-bottom:none;font-family:Bitter,serif;font-size:9.6px;color:#333;display:flex;align-items:center;background:#fff}
.tab.on{background:var(--green);color:#213a10;border-color:var(--green)}
.panel{border:2px solid var(--green);background:#fff}
.news{left:118px;top:815px;width:272px;height:172px;padding:7px 10px}
.news .item{border-bottom:1px solid #e5e5e5;padding-bottom:5px;margin-bottom:6px}
.news .item:last-of-type{border:none}
.news .date{font-size:7.5px;color:#222}
.news p{font-size:8.4px;line-height:11.4px;color:#444}
.dots{position:absolute;right:16px;bottom:6px;display:flex;gap:3px}
.dots i{width:5px;height:5px;border-radius:50%;background:#b5ca9a;display:block}
.dots i:first-child{background:var(--green-deep)}
.directors{left:401px;top:815px;width:194px;height:172px;padding:9px 10px}
.person{display:flex;gap:10px;margin-bottom:9px}
.person .photo{width:42px;height:42px;background:linear-gradient(#c9ccd0,#4b5b74);border:1px solid #888}
.person .name{font-family:Bitter,serif;font-size:9px;color:#555;margin-top:4px}
.person .meta{font-size:8.4px;line-height:12px;color:#555}
.support{left:608px;top:794px;width:151px;height:96px;border:2px solid var(--line);border-top:none;background:#ececec}
.support h3{font-family:Bitter,serif;font-size:11px;color:#555;background:#fff;height:25px;display:flex;align-items:center;padding-left:6px;font-weight:700}
.support .body{background:var(--green);height:63px;text-align:center;color:#fff;font-weight:700;font-size:9.4px;line-height:12px;padding-top:5px}
.support .btn{display:inline-block;margin-top:5px;background:var(--green-deep);padding:3px 8px;font-family:Bitter,serif;font-size:11px;letter-spacing:.5px;border-radius:2px}
.follow{left:608px;top:904px;width:147px;height:83px;background:linear-gradient(#4c6f2f,#36561f);color:#fff;padding:6px 7px}
.follow h3{font-weight:400;font-size:12.6px}
.follow p{font-size:7.5px;line-height:10px;margin-top:4px}
.socials{display:flex;gap:6px;margin-top:5px}
.socials i{width:16px;height:16px;border-radius:3px;background:#dfe8d2;display:block}

/* footer */
.footer{left:0;top:1014px;width:878px;height:160px;background:var(--footer);color:#fff}
.footer h4{font-weight:400;font-size:10.5px;padding-bottom:4px;border-bottom:1px dashed #b8cf98;display:inline-block}
.quick{position:absolute;left:118px;top:10px}
.quick ul{list-style:none;margin-top:8px;font-size:8.6px;line-height:14.4px}
.reviews{position:absolute;left:234px;top:10px;width:186px}
.reviews .arrows{position:absolute;right:0;top:0;font-size:11px;letter-spacing:6px}
.quote{margin-top:10px;background:var(--field);border-radius:8px;padding:8px 7px;font-size:8.6px;line-height:12px;height:82px;position:relative}
.quote:after{content:"";position:absolute;left:12px;bottom:-8px;border:8px solid transparent;border-top-color:var(--field);border-left-color:var(--field)}
.reviews .by{font-family:Bitter,serif;font-size:10px;margin-top:10px}
.inquiry{position:absolute;left:458px;top:10px;width:135px}
.field{background:var(--field);height:18px;margin-top:5px;font-size:7.5px;font-style:italic;padding:5px 9px;border:1px solid #a8c585}
.field.first{margin-top:10px}
.field.msg{height:49px}
.submit{display:inline-block;margin-top:5px;background:var(--green-deep);font-size:9.5px;padding:3px 8px}
.foot-name{position:absolute;left:636px;top:42px;width:130px;text-align:center;font-family:Bitter,serif;font-weight:700;font-size:22px;line-height:24px;color:#a3c07f;text-transform:uppercase}
.bottom{left:0;top:1174px;width:878px;height:26px;background:var(--footer-bar);color:#fff;font-size:7.5px;text-align:center;line-height:26px}
</style>
</head>
<body>

<header>
  <div class="abs brand">Lend a<br>Lantern</div>
  <div class="abs btn-donate">DONATE NOW</div>
  <div class="abs phone">
    <svg width="22" height="22" viewBox="0 0 22 22"><circle cx="11" cy="11" r="10" fill="none" stroke="#6f9a3e" stroke-width="1.5"/><path d="M7.5 6.5c1-.8 1.6-.5 2.2.6l.6 1.2c.3.7 0 1.1-.6 1.5.6 1.5 1.5 2.5 2.8 3.1.4-.6.8-.9 1.5-.6l1.2.6c1.1.6 1.4 1.2.6 2.2-1.6 1.9-4.4.6-6.3-1.5S5.6 8 7.5 6.5z" fill="#6f9a3e"/></svg>
    123-555-0147
  </div>
  <nav class="abs nav">
    <span class="active"><svg width="9" height="10" viewBox="0 0 9 10"><path d="M1 1l5 4-5 4" fill="none" stroke="#6f9a3e" stroke-width="2"/></svg>Home<svg width="7" height="10" viewBox="0 0 7 10"><path d="M1 1l4 4-4 4" fill="none" stroke="#6f9a3e" stroke-width="2"/></svg></span>
    <span>About Us</span><span>Training Programs</span><span>Photo &amp; Videos</span><span>Testimonials</span><span>Contact Us</span>
  </nav>
</header>

<section>
  <div class="abs hero" role="img" aria-label="Coach kneeling on a grass pitch with a circle of young soccer players holding balls"></div>
  <svg class="abs hero-arrow" style="left:92px" width="18" height="28" viewBox="0 0 18 28"><path d="M15 2L4 14l11 12" fill="none" stroke="#8fb863" stroke-width="5"/></svg>
  <svg class="abs hero-arrow" style="left:762px" width="18" height="28" viewBox="0 0 18 28"><path d="M3 2l11 12L3 26" fill="none" stroke="#8fb863" stroke-width="5"/></svg>
  <div class="abs mission">OUR MISSION: IMPROVE YOU WHILE IMPROVING SOMEONE ELSE</div>
</section>

<section class="abs welcome">
  <h2>Welcome to LEND A <span>LANTERN</span></h2>
  <p>Lorem ipsum dolor sit amet, consectetuer adipiscing elit, sed diam nonummy nibh euisiainciaadunt ut laoreet dolore magna aliquam erat volutpat. Ut wisi enim ad minim veniam, quigs nostruexerci taation ullamcorper suscipit lobortis nisl ut aliquip accumsan et iusto odio dvignissim qui blanditent luptreatum zzril delenit augue duis dolore te feugait nulla facilidolore magna aliquam erat volutpat. Ut wisi enim ad minim veniam, quis nostruexercadi tation ullamcorper suscipit lobortis nisl ut aliquip accumsan et iusto odio dignissim qui blanditent lure ptatum zzril delenit augue duis dolore te feugait nulla facilisi.......<span class="more">read more &gt;&gt;</span></p>
  <p class="lead">We are nonprofit organization providing soccer training opportunities to youth soccer players looking to improve their game while also affecting the lives of the less fortunate in a positive way</p>
</section>

<h2 class="abs video-title">View <span>Video</span></h2>
<div class="abs video" role="img" aria-label="Video still of a coach talking to young players in red kits">
  <svg style="position:absolute;left:90px;top:45px" width="26" height="26" viewBox="0 0 26 26"><circle cx="13" cy="13" r="12" fill="rgba(0,0,0,.75)" stroke="#fff" stroke-width="1"/><path d="M10 8l8 5-8 5z" fill="#fff"/></svg>
  <div class="progress"></div>
  <div class="bar">
    <svg style="position:absolute;left:12px;top:5px" width="120" height="10" viewBox="0 0 120 10"><path d="M0 0l8 5-8 5z" fill="#bbb"/><path d="M24 3h3l4-3v10l-4-3h-3z" fill="#bbb"/><text x="50" y="8" font-size="7" fill="#ccc" font-family="Arial">0:00</text></svg>
  </div>
</div>

<section class="abs gallery">
  <h2>Photo <span>Gallery</span></h2>
  <div class="nav-arrows">‹ ›</div>
  <div class="thumbs">
    <div class="thumb"><div role="img" aria-label="Coach showing a ball to a young player" style="background:linear-gradient(135deg,#3d5a7a,#9aa9b4)"></div></div>
    <div class="thumb"><div role="img" aria-label="Players standing on an evening pitch" style="background:linear-gradient(#2c3a22,#5c7a3c)"></div></div>
    <div class="thumb"><div role="img" aria-label="Children in red sitting on the grass" style="background:linear-gradient(#e8eef2,#7fa64a)"></div></div>
    <div class="thumb"><div role="img" aria-label="Coach with players in yellow shirts" style="background:linear-gradient(#e1c83c,#6e9a3a)"></div></div>
    <div class="thumb"><div role="img" aria-label="Youth team sitting together on the field" style="background:linear-gradient(#a9b86e,#5f7e3a)"></div></div>
  </div>
</section>

<div class="tabs" style="left:118px;top:794px">
  <div class="tab on">News &amp; Updates</div><div class="tab">Upcoming Event</div><div class="tab">Blog Posts</div>
</div>
<section class="abs panel news">
  <div class="item"><div class="date">25/07/2014</div><p>Lorem ipsum dolor sit amet, consectetuer adipiscing elit, sed diam nonummy nibh euisiainciaadunt ut laoreet dolore magna aliquam erat volutpat.</p></div>
  <div class="item"><div class="date">20/07/2014</div><p>Lorem ipsum dolor sit amet, consectetuer adipiscing elit, sed diam nonummy nibh euisiainciaadunt ut laoreet dolore magna aliquam erat volutpat.</p></div>
  <div class="item"><div class="date">23/07/2014</div><p>Lorem ipsum dolor sit amet, consectetuer adipiscing elit, sed diam nonummy nibh euisiainciaadunt ut laoreet dolore magna aliquam erat volutpat.</p></div>
  <div class="dots"><i></i><i></i><i></i><i></i></div>
</section>

<div class="tabs" style="left:401px;top:794px">
  <div class="tab on">Directors</div><div class="tab">Board Members</div>
</div>
<section class="abs panel directors">
  <div class="person"><div class="photo" role="img" aria-label="Director portrait"></div><div><div class="name">Mr. Lorem Ispim</div><div class="meta">Degree<br>Lorem Ispum</div></div></div>
  <div class="person"><div class="photo" role="img" aria-label="Director portrait"></div><div><div class="name">Mr. Lorem Ispim</div><div class="meta">Degree<br>Lorem Ispum</div></div></div>
  <div class="person"><div class="photo" role="img" aria-label="Director portrait"></div><div><div class="name">Mr. Lorem Ispim</div><div class="meta">Degree<br>Lorem Ispum</div></div></div>
  <div class="dots"><i></i><i></i><i></i><i></i></div>
</section>

<aside class="abs support">
  <h3>Help Support Our Cause</h3>
  <div class="body">Join the Cause And<br>Make A Donation<br><span class="btn">DONATE NOW</span></div>
</aside>
<aside class="abs follow">
  <h3>Follow Lend a Lantern</h3>
  <p>Keep Up With Social Events<br>And Happenings</p>
  <div class="socials"><i></i><i></i><i></i><i></i><i></i></div>
</aside>

<footer class="abs footer">
  <div class="quick">
    <h4>Quick Links</h4>
    <ul><li>Home</li><li>About Us</li><li>Packages</li><li>Photo &amp; Videos</li><li>Receptions</li><li>Testimonials</li><li>Contact Us</li></ul>
  </div>
  <div class="reviews">
    <h4>Client Reviews</h4>
    <div class="arrows">‹ ›</div>
    <div class="quote">"Lorem ipsum dolor sit amet, consectetuer adipiscing elit, sed diam nonummy nibh euisiainciaadunt ut laoreet dolore magna aliquam erat volutpat. Ut wisi enim ad minim veniam, quigs nostruexerci taation ullamcorper.........."</div>
    <div class="by">Anna and Tom</div>
  </div>
  <div class="inquiry">
    <h4>Quick Inquiry</h4>
    <div class="field first">Name</div>
    <div class="field">Email</div>
    <div class="field msg">Message</div>
    <span class="submit">Submit</span>
  </div>
  <div class="foot-name">Lend a Lantern</div>
</footer>
<div class="abs bottom">Copyright © 2014 &nbsp;Lend a Lantern &nbsp; All Rights Reserved</div>

</body>
</html>
```